I am a surgeon that operates on gynaecological cancer. Wish a design and logo for letter head.

Design should include my name: Dr. Torin Halwell, qualifications: FKMLTPVB, DMR. and state that I am a Gynaecological Oncologist and Advanced Laparoscopic Surgeon.
As for a logo. As all cancer is related to DNA, I think that that double helix could be used to symbolise a female shape, exaggerating the abdomen to suggest a mass.

Reason: Extended to view changes I have asked for.

```html
<!DOCTYPE html>
<html lang="en">
<head>
<meta charset="utf-8">
<title>Dr. Torin Halwell – Stationery</title>
<link href="https://fonts.googleapis.com/css2?family=Arimo:wght@400;700&display=swap" rel="stylesheet">
<style>
  :root {
    --backdrop: #d4d4d4;
    --paper: #ffffff;
    --orange: #f79a00;
    --blue: #1c5c99;
    --ink: #555555;
    --footer-ink: #ffffff;
  }
  html, body {
    margin: 0;
    padding: 0;
    overflow: hidden;
  }
  body {
    width: 1200px;
    height: 1000px;
    background: var(--backdrop);
    font-family: "Arimo", Arial, sans-serif;
    position: relative;
  }
  .sheet {
    position: absolute;
    left: 60px;
    width: 1075px;
    height: 467px;
    background: var(--paper);
    overflow: hidden;
  }
  .envelope-back { top: 21px; }
  .letterhead { top: 519px; }
  .sheet svg.art {
    position: absolute;
    left: 0;
    top: 0;
    width: 1075px;
    height: 467px;
  }
  .flap-name {
    position: absolute;
    left: 0;
    width: 1075px;
    top: 110px;
    text-align: center;
    font-size: 30px;
    color: var(--blue);
  }
  .web-address {
    position: absolute;
    left: 0;
    width: 1075px;
    top: 424px;
    text-align: center;
    font-size: 22px;
    color: var(--blue);
  }
  .brand {
    position: absolute;
    left: 27px;
    top: 22px;
  }
  .brand-mark {
    position: absolute;
    left: 0;
    top: 12px;
    width: 40px;
    height: 40px;
    background: var(--orange);
  }
  .brand-name {
    position: absolute;
    left: 57px;
    top: 0;
    margin: 0;
    font-weight: 400;
    font-size: 40px;
    line-height: 40px;
    color: var(--blue);
    white-space: nowrap;
  }
  .brand-tagline {
    position: absolute;
    left: 13px;
    top: 94px;
    font-size: 7px;
    color: var(--ink);
    white-space: nowrap;
  }
  .credentials {
    position: absolute;
    left: 14px;
    top: 247px;
    color: var(--ink);
  }
  .credentials .name { font-size: 15px; margin: 0; }
  .credentials .quals { font-size: 10px; margin: 3px 0 0 64px; }
  .credentials .role { font-size: 11px; line-height: 15px; margin: 6px 0 0; }
  .footer-text {
    position: absolute;
    color: var(--footer-ink);
    font-size: 16px;
    line-height: 19px;
    margin: 0;
  }
  .footer-text b { font-weight: 700; }
  .address { left: 47px; top: 393px; }
  .tel { left: 324px; top: 424px; }
  .mob { left: 527px; top: 424px; }
  .online { right: 34px; top: 408px; text-align: right; line-height: 26px; }
</style>
</head>
<body>

<section class="sheet envelope-back">
  <svg class="art" viewBox="0 0 1075 467" aria-hidden="true">
    <path fill="var(--orange)" d="M0 0 H1075 C1072 42 1062 58 1035 66 L680 178 Q540 212 400 178 L45 66 C18 58 4 40 0 0 Z"/>
  </svg>
  <div class="flap-name">Dr. Torin Halwell</div>
  <div class="web-address">www.drtorinhalwell.com</div>
</section>

<section class="sheet letterhead">
  <svg class="art" viewBox="0 0 1075 467" aria-hidden="true">
    <path class="swoosh" fill="var(--blue)" d="M0 323 Q560 468 1075 355 Q560 446 0 352 Z"/>
    <path class="footer-band" fill="var(--orange)" d="M0 359 Q560 456 1075 363 V467 H0 Z"/>
  </svg>

  <div class="brand">
    <span class="brand-mark"></span>
    <h1 class="brand-name">Dr. Torin<br>Halwell</h1>
    <div class="brand-tagline">Gynaecological Oncologist and Advanced Laparoscopic Surgeon</div>
  </div>

  <div class="credentials">
    <p class="name">Dr. Torin Halwell</p>
    <p class="quals">FKMLTPVB, DMR.</p>
    <p class="role">Gynaecological Oncologist and<br>Advanced Laparoscopic Surgeon.</p>
  </div>

  <p class="footer-text address">ABC<br>any street<br>Country</p>
  <p class="footer-text tel"><b>Tel :</b> +000 000 0000</p>
  <p class="footer-text mob"><b>Mob :</b> +000 000 0000</p>
  <p class="footer-text online"><b>E-mail :</b> name@torinhalwell.com<br><b>Web :</b> www.drtorinhalwell.com</p>
</section>

</body>
</html>
```